K48 PowerPoint Presentation

As you can see the design of this PowerPoint isn't cohesive. There are a lot of images and words that give it a very jumbled and busy appeal. We want to turn this into a sharp, cohesive and visually appealing presentation without taking away too much of the information. Feel free to use the images to create your own artwork for the PowerPoint.

Please don't hesitate to contact me with any questions.

Industry/Entity Type

Graphic Design

```html
<!DOCTYPE html>
<html lang="en">
<head>
<meta charset="utf-8">
<title>K48 Presentation Slides</title>
<link rel="stylesheet" href="https://fonts.googleapis.com/css2?family=Open+Sans:wght@400;600;700&display=swap">
<style>
  :root {
    --canvas: #ffffff;
    --navy-dark: #15257a;
    --navy: #22389e;
    --navy-light: #3553c0;
    --title-gold: #ffd21a;
    --slide-light: #f7f7f7;
    --slide-mid: #e2e2e2;
    --slide-edge: #cfcfcf;
    --brand-ink: #24368f;
    --node-blue: #1a95d6;
    --mesh-blue: #9dcdec;
    --chevron-green: #74c043;
    --ink: #222222;
    --muted: #555555;
  }
  * { margin: 0; padding: 0; box-sizing: border-box; }
  html, body {
    width: 1026px; height: 1200px; overflow: hidden;
    background: var(--canvas);
    font-family: "Open Sans", Arial, sans-serif;
    color: var(--ink);
  }
  .deck { position: relative; width: 1026px; height: 1200px; }
  .slide {
    position: absolute; left: 133px; width: 760px; height: 570px; overflow: hidden;
    background: radial-gradient(ellipse at 50% 40%, var(--slide-light) 0%, var(--slide-mid) 75%, var(--slide-edge) 100%);
    box-shadow: 0 1px 4px rgba(0,0,0,.25);
  }
  .slide--platform { top: 20px; }
  .slide--links { top: 610px; }
  .slide-header {
    position: absolute; left: 0; top: 0; width: 760px; height: 64px;
    background: linear-gradient(90deg, var(--navy-light) 0%, var(--navy) 45%, var(--navy-dark) 100%);
  }
  .slide-title {
    position: absolute; left: 200px; right: 150px; top: 0; height: 64px;
    display: flex; align-items: center; justify-content: center;
    font-weight: 700; font-size: 17px; color: var(--title-gold); letter-spacing: .2px;
  }
  .partner-name {
    position: absolute; right: 22px; top: 14px;
    font-weight: 600; font-size: 15px; color: #ffffff;
  }
  .brand-tab { position: absolute; left: 65px; top: 0; width: 109px; height: 116px; }
  .brand-tab svg { display: block; }
  .brand-name {
    position: absolute; left: 0; top: 32px; width: 109px;
    display: flex; align-items: center; justify-content: center; gap: 5px;
    font-weight: 700; font-size: 19px; color: var(--brand-ink);
  }
  .brand-dot { width: 12px; height: 12px; border-radius: 50%; background: var(--brand-ink); }
  .page-number { position: absolute; right: 48px; bottom: 22px; font-size: 10px; color: var(--ink); }

  .platform-heading {
    position: absolute; left: 0; right: 0; top: 110px; text-align: center;
    font-size: 14px; color: var(--ink);
  }
  .device-visual {
    position: absolute; left: 163px; top: 146px; width: 380px; height: 234px;
    border-radius: 6px;
    background: linear-gradient(160deg, #3a3f46 0%, #8d96a3 45%, #dfe5ec 100%);
  }
  .feature-list {
    position: absolute; left: 0; top: 0; width: 760px; height: 570px;
    list-style: none;
  }
  .feature {
    position: absolute; display: flex; align-items: center; gap: 12px;
    width: 240px; white-space: nowrap;
    font-size: 10.5px; color: var(--ink); line-height: 1.35;
  }
  .feature-num {
    flex: 0 0 36px; width: 36px; height: 36px; border-radius: 50%;
    background: var(--node-blue); color: #fff; font-weight: 700; font-size: 10px;
    display: flex; align-items: center; justify-content: center;
  }
  .network { position: absolute; left: 0; top: 0; }
  .node-label { font-size: 10px; fill: var(--ink); text-anchor: middle; }
  .summary-title { font-size: 12.5px; font-weight: 700; fill: var(--ink); }
  .summary-item { font-size: 10px; fill: var(--muted); }
</style>
</head>
<body>
<main class="deck">

  <section class="slide slide--platform">
    <header class="slide-header">
      <h1 class="slide-title">K48 DISCOVERY PLATFORM</h1>
      <span class="partner-name">Norvale Systems</span>
    </header>
    <div class="brand-tab">
      <svg width="109" height="116" viewBox="0 0 109 116">
        <defs>
          <linearGradient id="tabFillA" x1="0" y1="0" x2="0" y2="1">
            <stop offset="0" stop-color="#ffffff"/><stop offset="1" stop-color="#dedede"/>
          </linearGradient>
        </defs>
        <polygon points="0,0 109,0 109,88 55,114 0,88" fill="url(#tabFillA)" stroke="#c9c9c9"/>
      </svg>
      <div class="brand-name"><span class="brand-dot"></span>K48</div>
    </div>

    <p class="platform-heading">MULTI-DEVICE, MOBILE and DESKTOP Ready!</p>
    <div class="device-visual" role="img" aria-label="Desktop monitor, tablet and phone showing the platform dashboard"></div>

    <ol class="feature-list">
      <li class="feature" style="left:141px;top:407px;"><span class="feature-num">1.</span>Modular Tool Architecture.</li>
      <li class="feature" style="left:141px;top:447px;"><span class="feature-num">2.</span>Extensible Widget Framework.</li>
      <li class="feature" style="left:141px;top:487px;"><span class="feature-num">3.</span>Real-Time Data Events.</li>
      <li class="feature" style="left:378px;top:403px;"><span class="feature-num">4.</span>Semantic &amp; Concept Searching.</li>
      <li class="feature" style="left:378px;top:445px;"><span class="feature-num">5.</span>Entity &amp; Facet Searching And Filtering</li>
      <li class="feature" style="left:378px;top:486px;"><span class="feature-num">6.</span><span>User Definable Data Dictionaries, Gazeteers<br>And Ontologies.</span></li>
    </ol>
    <span class="page-number">15</span>
  </section>

  <section class="slide slide--links">
    <svg class="network" width="760" height="570" viewBox="0 0 760 570">
      <path fill="none" stroke="var(--mesh-blue)" stroke-width="1.1" d="
        M305 166L396 186M305 166L463 248M305 166L463 368M305 166L396 429M305 166L305 451M305 166L214 429M305 166L147 368M305 166L147 248M305 166L214 186
        M396 186L463 248M396 186L463 368M396 186L396 429M396 186L305 451M396 186L214 429M396 186L147 368M396 186L147 248M396 186L214 186
        M463 248L463 368M463 248L396 429M463 248L305 451M463 248L214 429M463 248L147 368M463 248L147 248M463 248L214 186
        M463 368L396 429M463 368L305 451M463 368L214 429M463 368L147 368M463 368L147 248M463 368L214 186
        M396 429L305 451M396 429L214 429M396 429L147 368M396 429L147 248M396 429L214 186
        M305 451L214 429M305 451L147 368M305 451L147 248M305 451L214 186
        M214 429L147 368M214 429L147 248M214 429L214 186
        M147 368L147 248M147 368L214 186
        M147 248L214 186"/>

      <g class="chevrons" fill="none" stroke="var(--chevron-green)" stroke-width="6" stroke-linejoin="miter">
        <polyline points="82,298 92,308 82,318"/><polyline points="102,298 112,308 102,318"/><polyline points="122,298 132,308 122,318"/>
        <polyline points="485,298 495,308 485,318"/><polyline points="505,298 515,308 505,318"/><polyline points="525,298 535,308 525,318"/>
      </g>

      <g class="nodes" fill="var(--node-blue)" stroke="#ffffff" stroke-width="2">
        <circle cx="305" cy="166" r="30"/><circle cx="396" cy="186" r="30"/><circle cx="463" cy="248" r="30"/>
        <circle cx="463" cy="368" r="30"/><circle cx="396" cy="429" r="30"/><circle cx="305" cy="451" r="30"/>
        <circle cx="214" cy="429" r="30"/><circle cx="147" cy="368" r="30"/><circle cx="147" cy="248" r="30"/>
        <circle cx="214" cy="186" r="30"/>
      </g>
      <g class="node-icons" fill="none" stroke="#ffffff" stroke-width="2.5">
        <circle cx="305" cy="166" r="9"/><circle cx="396" cy="186" r="9"/><circle cx="463" cy="248" r="9"/>
        <circle cx="463" cy="368" r="9"/><circle cx="396" cy="429" r="9"/><circle cx="305" cy="451" r="9"/>
        <circle cx="214" cy="429" r="9"/><circle cx="147" cy="368" r="9"/><circle cx="147" cy="248" r="9"/>
      </g>
      <text x="214" y="194" text-anchor="middle" font-size="22" font-weight="700" fill="#ffffff">$</text>

      <text class="node-label" x="305" y="128">Strategy</text>
      <text class="node-label" x="396" y="148">References</text>
      <text class="node-label" x="463" y="210">Equipment</text>
      <text class="node-label" x="214" y="148">Budget</text>
      <text class="node-label" x="147" y="210">Locations</text>
      <text class="node-label" x="463" y="412">Training</text>
      <text class="node-label" x="396" y="473">Applications</text>
      <text class="node-label" x="305" y="495">Doctrine</text>
      <text class="node-label" x="214" y="473">Standards</text>
      <text class="node-label" x="147" y="412">Organizations</text>

      <text class="summary-title" x="567" y="273">All data points linked</text>
      <circle cx="571" cy="293" r="5" fill="none" stroke="var(--node-blue)" stroke-width="1.5"/>
      <text class="summary-item" x="582" y="297">Associated analysis of</text>
      <text class="summary-item" x="582" y="310">any or all data points.</text>
      <circle cx="571" cy="328" r="5" fill="none" stroke="var(--node-blue)" stroke-width="1.5"/>
      <text class="summary-item" x="582" y="332">Unrestricted analysis</text>
      <text class="summary-item" x="582" y="345">options/comparisons.</text>
    </svg>

    <header class="slide-header">
      <h1 class="slide-title">LINKING MULTIPLE DATA POINTS</h1>
      <span class="partner-name">Norvale Systems</span>
    </header>
    <div class="brand-tab">
      <svg width="109" height="116" viewBox="0 0 109 116">
        <defs>
          <linearGradient id="tabFillB" x1="0" y1="0" x2="0" y2="1">
            <stop offset="0" stop-color="#ffffff"/><stop offset="1" stop-color="#dedede"/>
          </linearGradient>
        </defs>
        <polygon points="0,0 109,0 109,88 55,114 0,88" fill="url(#tabFillB)" stroke="#c9c9c9"/>
      </svg>
      <div class="brand-name"><span class="brand-dot"></span>K48</div>
    </div>
    <span class="page-number">7</span>
  </section>

</main>
</body>
</html>
```